1 Page Software Marketing/Sales Flyer Slick

Copperline Dynamics manufactures several software packages that we sell. We need a 1 page sales/marketing flyer slick that we will allow people to download from our site or as physical leave behinds in meetings. This 1 page slick should be visually (graphically) pleasing while carrying our message for selling our software product.

Target Market(s)

Enterprise Business Customers

Industry/Entity Type

Voip

Requirements
Must have
• Graphical representation of some hot point features, 1 Page - See PDF Detailed Description
Nice to have
• See PDF Detailed Description

```html
<!DOCTYPE html>
<html lang="en">
<head>
<meta charset="utf-8">
<title>Copperline Dynamics – CLD CDR Flyer</title>
<link href="https://fonts.googleapis.com/css2?family=Lato:wght@400;700&family=Montserrat:wght@400;500&family=Roboto:wght@300&display=swap" rel="stylesheet">
<style>
  :root{
    --stage:#f6f6f6;
    --paper:#ffffff;
    --navy:#1c4c8c;
    --band:#195d96;
    --mist:#e2e9f1;
    --arc:#e0e8f0;
    --ink:#2b2b2b;
    --green:#7cb874;
    --red:#a51c2a;
    --gold:#d4b52c;
    --grey:#bdbdbd;
  }
  *{box-sizing:border-box;margin:0;padding:0}
  html,body{width:1200px;height:1000px;overflow:hidden;background:var(--stage)}
  .flyer{position:absolute;left:303px;top:62px;width:593px;height:874px;background:var(--paper);overflow:hidden;font-family:"Lato",sans-serif;color:var(--ink)}
  .abs{position:absolute}
  .backdrop-arc{left:-90px;top:256px;width:773px;height:773px;border-radius:50%;background:var(--arc)}
  .brand-dot{left:53px;top:38px;width:62px;height:62px;border-radius:50%;background:var(--navy)}
  .brand-name{left:125px;top:52px;font-family:"Roboto",sans-serif;font-weight:300;font-size:26px;color:var(--navy);letter-spacing:-.3px}
  .intro{left:55px;top:120px;width:493px;font-size:11.4px;line-height:14px;color:#333}
  .section-title{font-weight:700;font-size:15px;color:var(--navy)}
  .feature-icon{width:60px;height:60px;border-radius:50%;background:radial-gradient(circle at 50% 40%,#2d6db3,#163f7a);box-shadow:0 0 0 4px #3b8ddb;display:flex;align-items:center;justify-content:center;color:#fff}
  .feature-title{font-family:"Montserrat",sans-serif;font-size:14px;line-height:17px;color:var(--navy);width:160px}
  .feature-text{font-size:11.6px;line-height:13.5px;color:#222;width:140px}
  .system-band{left:0;top:430px;width:593px;height:194px;background:var(--band)}
  .system-band .section-title{color:#fff}
  .system-text{font-size:12px;line-height:14.5px;color:#fff;width:150px}
  .apps{left:0;top:624px;width:593px;height:244px;background:var(--mist)}
  .apps-title{left:52px;top:14px;font-weight:700;font-size:14px;color:#fff}
  .chart-panel{left:33px;top:47px;width:522px;height:167px;background:#fff}
  .footer-rule{left:0;top:868px;width:593px;height:6px;background:var(--band)}
  .vendor-name{font-family:"Lato",sans-serif;font-weight:700;font-size:16px;letter-spacing:1px;color:#fff}
</style>
</head>
<body>
<main class="flyer">
  <div class="abs backdrop-arc"></div>

  <div class="abs brand-dot"></div>
  <div class="abs brand-name">Copperline Dynamics</div>

  <p class="abs intro">Easily and quickly search for call detail reporting information that your department or organization requires. CLD CDR is a modern CDR and CMR reporting package that is visually stunning and equally powerful. Designed and created by Trellon certified software developers, CLD CDR is guaranteed to deliver affordable software with real world features</p>

  <h2 class="abs section-title" style="left:56px;top:205px">CLD CDR Software Feature Functionality</h2>

  <div class="abs feature-icon" style="left:100px;top:242px">
    <svg width="32" height="32" viewBox="0 0 32 32" fill="none" stroke="#fff" stroke-width="2.4"><circle cx="14" cy="14" r="10"/><line x1="21" y1="21" x2="28" y2="28" stroke-linecap="round"/><path d="M10 9c-1 2 1 7 5 9l2-2-2-2-1 1c-1-1-2-2-2-3l1-1-2-2z" fill="#fff" stroke="none"/></svg>
  </div>
  <div class="abs feature-icon" style="left:260px;top:242px;font-family:'Montserrat',sans-serif;font-weight:500;font-size:21px">911</div>
  <div class="abs feature-icon" style="left:420px;top:242px">
    <svg width="30" height="30" viewBox="0 0 30 30" fill="#fff"><path d="M6 10c-1 4 4 12 10 14l3-3-3-3-2 2c-2-1-4-4-5-6l2-2-3-3z"/><rect x="17" y="11" width="2" height="6"/><rect x="20" y="8" width="2" height="9"/><rect x="23" y="10" width="2" height="7"/><rect x="16" y="18" width="10" height="1.5"/></svg>
  </div>

  <h3 class="abs feature-title" style="left:56px;top:316px">Searching for a call</h3>
  <h3 class="abs feature-title" style="left:231px;top:315px">Emergency number notifications</h3>
  <h3 class="abs feature-title" style="left:389px;top:315px">Call diagnostics feature for CMR</h3>

  <p class="abs feature-text" style="left:58px;top:356px">Search for a specific number or group of numbers by Department and/or by a data</p>
  <p class="abs feature-text" style="left:231px;top:356px">Receive email alerts when 911 or other designated emergency numbers are dialed</p>
  <p class="abs feature-text" style="left:388px;top:356px">Threshold based automatic alerting for voice and video calls</p>

  <section class="abs system-band">
    <h2 class="abs section-title" style="left:52px;top:13px">CLD CDR System Features</h2>
    <svg class="abs" style="left:97px;top:58px" width="50" height="38" viewBox="0 0 50 38" fill="none" stroke="#fff" stroke-width="2.5"><rect x="2" y="2" width="46" height="34"/><line x1="2" y1="9" x2="48" y2="9"/><line x1="2" y1="29" x2="48" y2="29"/><text x="25" y="24" fill="#fff" stroke="none" text-anchor="middle" font-family="Lato,sans-serif" font-weight="700" font-size="12">SQL</text></svg>
    <svg class="abs" style="left:266px;top:58px" width="38" height="38" viewBox="0 0 38 38" fill="none" stroke="#fff" stroke-width="4"><path d="M6 17a13 13 0 0 1 23-7"/><path d="M32 21a13 13 0 0 1-23 7"/><path d="M30 3v9h-9" stroke-width="3.5"/><path d="M8 35v-9h9" stroke-width="3.5"/></svg>
    <div class="abs vendor-name" style="left:412px;top:68px">TRELLON</div>
    <p class="abs system-text" style="left:52px;top:114px">Imports TUCM CDR records into flexible a RelayDB database every 10 seconds</p>
    <p class="abs system-text" style="left:226px;top:114px">Automatically updates associated CDR Record(s) when new fields are added</p>
    <p class="abs system-text" style="left:387px;top:114px">Trellon UCM Publisher pushes new CDR/CMR data every 10 seconds</p>
  </section>

  <section class="abs apps">
    <h2 class="abs apps-title">CLD CDR APPS</h2>
    <div class="abs chart-panel">
      <svg width="522" height="167" viewBox="0 0 522 167" font-family="Lato,sans-serif">
        <!-- pie chart -->
        <g transform="translate(126,87)">
          <path d="M0 0 L0 -50 A50 50 0 1 1 -22 -45 Z" fill="var(--green)" stroke="#fff"/>
          <path d="M0 0 L-22 -45 A50 50 0 0 1 -49 -10 Z" fill="var(--red)" stroke="#fff"/>
          <path d="M0 0 L0 -50 A50 50 0 0 0 -22 -45 Z" fill="var(--gold)" stroke="#fff"/>
        </g>
        <polyline points="114,39 84,15 52,15" fill="none" stroke="var(--gold)" stroke-width=".8"/>
        <text x="22" y="17" font-size="5.5" fill="#333">REDIRECTED</text>
        <polyline points="90,66 64,38 47,38" fill="none" stroke="var(--red)" stroke-width=".8"/>
        <text x="14" y="40" font-size="5.5" fill="#333">NOT ANSWER</text>
        <polyline points="165,130 170,151 198,151" fill="none" stroke="var(--green)" stroke-width=".8"/>
        <text x="201" y="153" font-size="5.5" fill="#333">ANSWERED</text>
        <rect x="108" y="12" width="34" height="22" rx="2" fill="#3a3a3a"/>
        <path d="M121 34 l4 4 4-4z" fill="#3a3a3a"/>
        <text x="125" y="21" font-size="6" fill="#fff" text-anchor="middle">Answered</text>
        <text x="125" y="31" font-size="8" font-weight="700" fill="#fff" text-anchor="middle">240</text>
        <!-- line chart -->
        <g font-size="4.5" fill="#444">
          <g stroke="#e6e6e6" stroke-width=".6">
            <line x1="276" y1="24" x2="462" y2="24"/><line x1="276" y1="37" x2="462" y2="37"/>
            <line x1="276" y1="51" x2="462" y2="51"/><line x1="276" y1="64" x2="462" y2="64"/>
            <line x1="276" y1="78" x2="462" y2="78"/><line x1="276" y1="91" x2="462" y2="91"/>
            <line x1="276" y1="105" x2="462" y2="105"/><line x1="276" y1="118" x2="462" y2="118"/>
            <line x1="276" y1="131" x2="462" y2="131"/>
            <line x1="282" y1="24" x2="282" y2="131"/><line x1="318" y1="24" x2="318" y2="131"/>
            <line x1="354" y1="24" x2="354" y2="131"/><line x1="390" y1="24" x2="390" y2="131"/>
            <line x1="426" y1="24" x2="426" y2="131"/><line x1="462" y1="24" x2="462" y2="131"/>
          </g>
          <text x="264" y="26">400</text><text x="264" y="39">350</text><text x="264" y="53">300</text>
          <text x="264" y="66">250</text><text x="264" y="80">200</text><text x="264" y="93">150</text>
          <text x="264" y="107">100</text><text x="266" y="120">50</text><text x="268" y="133">0</text>
          <text x="258" y="80" transform="rotate(-90 258 80)">Calls</text>
          <text x="272" y="140">2017-09-10</text><text x="308" y="140">2017-09-11</text>
          <text x="344" y="140">2017-09-12</text><text x="380" y="140">2017-09-13</text>
          <text x="416" y="140">2017-09-14</text><text x="452" y="140">2017-09-15</text>
          <text x="366" y="148">Time</text>
        </g>
        <polyline points="282,24 318,110 354,120 390,112 426,112 462,114" fill="none" stroke="var(--grey)" stroke-width="1"/>
        <polyline points="282,66 318,120 354,125 390,117 426,122 462,124" fill="none" stroke="var(--green)" stroke-width="1"/>
        <polyline points="282,121 318,126 354,128 390,124 426,124 462,126" fill="none" stroke="var(--gold)" stroke-width="1"/>
        <polyline points="282,123 318,129 354,130 390,130 426,128 462,129" fill="none" stroke="var(--red)" stroke-width="1"/>
        <g font-size="4.5" fill="#333">
          <text x="471" y="26" font-size="5.5" font-weight="700">Legend</text>
          <rect x="470" y="29" width="40" height="33" fill="#f1f1f1"/>
          <rect x="473" y="32" width="4" height="4" fill="var(--green)"/><text x="480" y="36">Answered</text>
          <rect x="473" y="39" width="4" height="4" fill="var(--red)"/><text x="480" y="43">No Answer</text>
          <rect x="473" y="46" width="4" height="4" fill="var(--gold)"/><text x="480" y="50">Redirected</text>
          <rect x="473" y="53" width="4" height="4" fill="var(--grey)"/><text x="480" y="57">All</text>
        </g>
      </svg>
    </div>
  </section>

  <div class="abs footer-rule"></div>
</main>
</body>
</html>
```